Header For Web Site

I need a header for the web site www.feltonpipeworks.example/demo
It must include the following
Existig Logo (I will upload the .png)
Text: Serving Calgary and Surrounding Areas for Over 30 Years!
24 Hour Service
Call 403.818.2727 (Note this isn't the actual phone number I will need to be able to change the Phone number once the site is ready to put in a tracking number so I am hoping I get a PSD file with this where the text is editable)
We wnat the feel to be warm and geared more towards a residential customer rather than an industial customer.
We would like blue tones but are open to anything warm.

Size: Aprroximately 960x300

Industry/Entity Type

Residential

Requirements
Must have
• Rounded Corners to match the content area on the site

```html
<!DOCTYPE html>
<html lang="en">
<head>
<meta charset="utf-8">
<title>Felton Pipeworks — Header</title>
<link rel="stylesheet" href="https://fonts.googleapis.com/css2?family=Arimo:wght@400;700&display=swap">
<style>
  :root {
    --ink: #0d0d0d;
    --panel: rgba(255, 255, 255, 0.82);
    --panel-edge: rgba(255, 255, 255, 0.35);
    --warm-light: #f3e3d6;
    --warm-mid: #c9a38d;
    --warm-deep: #6b4f43;
    --stone-dark: #3a322e;
    --stone-mid: #8a7e76;
    --logo-ink: #2b3140;
    --page: #ffffff;
  }
  html, body {
    margin: 0;
    padding: 0;
    width: 1200px;
    height: 375px;
    overflow: hidden;
    background: var(--page);
  }
  .site-header {
    position: relative;
    width: 1200px;
    height: 375px;
    overflow: hidden;
    border-radius: 16px;
    font-family: "Arimo", Arial, Helvetica, sans-serif;
  }
  .bathroom-scene {
    position: absolute;
    inset: 0;
    background:
      radial-gradient(ellipse 330px 200px at 610px 175px, rgba(255,255,255,0.85), rgba(255,255,255,0) 70%),
      linear-gradient(90deg, var(--warm-mid) 0%, var(--warm-light) 22%, var(--warm-light) 45%, #e8d4c4 58%, var(--stone-mid) 72%, var(--stone-dark) 86%, var(--warm-deep) 100%);
  }
  .headline-panel {
    position: absolute;
    left: 0;
    top: 0;
    width: 698px;
    height: 78px;
    background: var(--panel);
    border-right: 2px solid var(--panel-edge);
  }
  .headline {
    position: absolute;
    left: 18px;
    top: 6px;
    margin: 0;
    font-size: 65px;
    line-height: 68px;
    font-weight: 700;
    color: var(--ink);
    letter-spacing: 0.3px;
    white-space: nowrap;
  }
  .brand {
    position: absolute;
    left: 420px;
    top: 112px;
    width: 400px;
  }
  .brand-line {
    display: flex;
    align-items: center;
    gap: 12px;
  }
  .brand-mark {
    width: 20px;
    height: 20px;
    background: var(--logo-ink);
    flex: none;
  }
  .brand-name {
    font-size: 34px;
    line-height: 40px;
    font-weight: 700;
    color: var(--logo-ink);
    letter-spacing: 2px;
    white-space: nowrap;
  }
  .tagline {
    margin: 10px 0 0 0;
    padding-top: 6px;
    border-top: 2px solid var(--logo-ink);
    font-size: 14px;
    line-height: 18px;
    font-weight: 400;
    color: var(--logo-ink);
    white-space: nowrap;
  }
  .call-panel {
    position: absolute;
    right: 0;
    bottom: 0;
    width: 580px;
    height: 84px;
    background: var(--panel);
    border-left: 2px solid var(--panel-edge);
  }
  .call-line {
    position: absolute;
    right: 16px;
    top: 9px;
    margin: 0;
    font-size: 64px;
    line-height: 68px;
    font-weight: 700;
    color: var(--ink);
    white-space: nowrap;
  }
</style>
</head>
<body>
  <header class="site-header">
    <div class="bathroom-scene" role="img" aria-label="Warmly lit modern bathroom with a soaking tub and a stone vessel sink"></div>

    <div class="headline-panel">
      <h1 class="headline">24 HOURS SERVICE!</h1>
    </div>

    <div class="brand">
      <div class="brand-line">
        <span class="brand-mark"></span>
        <span class="brand-name">FELTON PIPEWORKS</span>
      </div>
      <p class="tagline">Serving Calgary and Surrounding Areas for Over 30 Years!</p>
    </div>

    <div class="call-panel">
      <p class="call-line">Call 403.818.2727</p>
    </div>
  </header>
</body>
</html>
```